Brivora Australia Company Values.

We have just completed our company purpose, beliefs and values (for the first time, we have not had these before)
We are now wanting to add images to each company value as a visual
so they are easily identified and understood for all our staff - we need them to remember the 5 Values.
We are a manufacturer of dental materials and infection control products, based in Melbourne.

What we would like:
- A Poster (that can be placed in our staff lunch rooms)
- The values to be lined up Horizontally
- Image on the top of the words
- Wording does not all need to be the same text font
- No image photographs - please use image graphics
- No images with people
- No dental related graphics

Target audience: Brivora staff

Our Values are:
Think Big
Have a go, learn and adapt
If you're gonna do it, do it bloody well
Empower Others
Be a good human

I have uploaded some examples.

Target Market(s)

Brivora Team members

Industry/Entity Type

Healthcare

Colors

Designer to choose colors to be used in the design.

Requirements
Must have
• Clear horizontal layout, space between each value
Should not have
• No images with humans or dental

```html
<!DOCTYPE html>
<html lang="en">
<head>
<meta charset="UTF-8">
<title>Brivora Australia – Core Values</title>
<link href="https://fonts.googleapis.com/css2?family=Montserrat:wght@600;700;800&family=Open+Sans:wght@400;600&display=swap" rel="stylesheet">
<style>
  :root {
    --page: #e9ebee;
    --navy: #12233f;
    --navy-deep: #0c182d;
    --navy-light: #1c3358;
    --banner: #1f5fae;
    --banner-edge: #6fa6e6;
    --card: #ffffff;
    --body-text: #6b7280;
    --purple: #6c2d91;
    --teal: #17a59b;
    --orange: #f28a1a;
    --red: #e2263b;
    --green: #12806f;
    --white: #ffffff;
  }
  * { margin: 0; padding: 0; box-sizing: border-box; }
  html, body { width: 800px; height: 1200px; overflow: hidden; }
  body {
    background: var(--page);
    font-family: "Open Sans", Arial, sans-serif;
    position: relative;
  }
  .poster {
    position: absolute;
    left: 20px; top: 338px;
    width: 760px; height: 524px;
    background: radial-gradient(ellipse at 50% 40%, var(--navy-light), var(--navy) 60%, var(--navy-deep));
    overflow: hidden;
  }
  .poster__texture {
    position: absolute; inset: 0;
    background: linear-gradient(135deg, rgba(255,255,255,0.04), rgba(255,255,255,0) 50%, rgba(255,255,255,0.04));
  }
  .title-banner {
    position: absolute; left: 50%; top: 26px;
    transform: translateX(-50%);
    width: 320px; height: 60px;
  }
  .title-banner svg { position: absolute; inset: 0; }
  .title-banner h1 {
    position: relative;
    font-family: "Montserrat", Arial, sans-serif;
    font-weight: 800; font-size: 32px;
    letter-spacing: 3px;
    color: var(--white);
    text-align: center; line-height: 60px;
  }
  .divider { position: absolute; left: 36px; top: 104px; width: 688px; height: 12px; }
  .values {
    position: absolute; left: 36px; top: 124px;
    display: flex; gap: 22px;
  }
  .value { position: relative; width: 120px; height: 318px; }
  .value__shape { position: absolute; inset: 0; }
  .value__icon {
    position: absolute; left: 38px; top: 30px;
    width: 44px; height: 44px; border-radius: 50%;
    background: rgba(255,255,255,0.85);
  }
  .value__name {
    position: absolute; left: 8px; right: 8px; top: 124px;
    font-family: "Montserrat", Arial, sans-serif;
    font-weight: 700; font-size: 12.5px; line-height: 1.25;
    text-align: center;
  }
  .value__text {
    position: absolute; left: 10px; right: 10px; top: 192px;
    font-size: 7.5px; line-height: 1.45;
    color: var(--body-text); text-align: center;
  }
  .value--purple .value__name { color: var(--purple); }
  .value--teal .value__name { color: var(--teal); }
  .value--orange .value__name { color: var(--orange); }
  .value--red .value__name { color: var(--red); }
  .value--green .value__name { color: var(--green); }
  .footer {
    position: absolute; left: 0; right: 0; bottom: 0; height: 40px;
    background: var(--navy-deep);
    display: flex; align-items: center; justify-content: space-between;
    padding: 0 24px;
    font-size: 9px; color: #c9d3e3; letter-spacing: 1px;
  }
  .brand { display: flex; align-items: center; gap: 6px; }
  .brand__mark { width: 12px; height: 12px; background: var(--white); }
  .brand__name { font-family: "Montserrat", Arial, sans-serif; font-weight: 700; font-size: 13px; color: var(--white); letter-spacing: 0; }
  .footer__company { font-weight: 600; text-transform: uppercase; }
</style>
</head>
<body>
<main class="poster">
  <div class="poster__texture"></div>

  <header class="title-banner">
    <svg viewBox="0 0 320 60" width="320" height="60">
      <polygon points="22,2 298,2 318,30 298,58 22,58 2,30" fill="none" stroke="var(--banner-edge)" stroke-width="2"/>
      <polygon points="26,7 294,7 311,30 294,53 26,53 9,30" fill="var(--banner)"/>
    </svg>
    <h1>CORE VALUES</h1>
  </header>

  <svg class="divider" viewBox="0 0 688 12" width="688" height="12">
    <line x1="0" y1="6" x2="688" y2="6" stroke="#3a5680" stroke-width="1.5"/>
    <polygon points="100,2 108,6 100,10" fill="var(--purple)"/>
    <polygon points="242,2 250,6 242,10" fill="var(--teal)"/>
    <polygon points="384,2 392,6 384,10" fill="var(--orange)"/>
    <polygon points="526,2 534,6 526,10" fill="var(--red)"/>
    <polygon points="668,2 676,6 668,10" fill="var(--green)"/>
  </svg>

  <section class="values">
    <article class="value value--purple">
      <svg class="value__shape" viewBox="0 0 120 318" width="120" height="318">
        <polygon points="0,70 20,56 100,56 120,70 120,278 60,318 0,278" fill="var(--card)"/>
        <polygon points="60,0 108,26 108,80 60,106 12,80 12,26" fill="var(--purple)"/>
      </svg>
      <div class="value__icon" role="img" aria-label="Lightbulb icon"></div>
      <h2 class="value__name">Think<br>Big</h2>
      <p class="value__text">Dream beyond limits and set ambitious goals. Look for bold ideas that move our business and our people forward together.</p>
    </article>

    <article class="value value--teal">
      <svg class="value__shape" viewBox="0 0 120 318" width="120" height="318">
        <polygon points="0,70 20,56 100,56 120,70 120,278 60,318 0,278" fill="var(--card)"/>
        <polygon points="60,0 108,26 108,80 60,106 12,80 12,26" fill="var(--teal)"/>
      </svg>
      <div class="value__icon" role="img" aria-label="Head with gears icon"></div>
      <h2 class="value__name">Have a go,<br>Learn and<br>Adapt</h2>
      <p class="value__text">Try new things without fear of failing. Learn from every step, share what works and adapt quickly when needed always.</p>
    </article>

    <article class="value value--orange">
      <svg class="value__shape" viewBox="0 0 120 318" width="120" height="318">
        <polygon points="0,70 20,56 100,56 120,70 120,278 60,318 0,278" fill="var(--card)"/>
        <polygon points="60,0 108,26 108,80 60,106 12,80 12,26" fill="var(--orange)"/>
      </svg>
      <div class="value__icon" role="img" aria-label="Clipboard checklist icon"></div>
      <h2 class="value__name">If You're gonna<br>do it, do it<br>Bloody Well</h2>
      <p class="value__text">Take pride in everything we make. Give full effort, check the details and deliver quality our customers can always trust.</p>
    </article>

    <article class="value value--red">
      <svg class="value__shape" viewBox="0 0 120 318" width="120" height="318">
        <polygon points="0,70 20,56 100,56 120,70 120,278 60,318 0,278" fill="var(--card)"/>
        <polygon points="60,0 108,26 108,80 60,106 12,80 12,26" fill="var(--red)"/>
      </svg>
      <div class="value__icon" role="img" aria-label="Team group icon"></div>
      <h2 class="value__name">Empower<br>others</h2>
      <p class="value__text">Support each other to grow. Give people the trust, tools and room they need to lead and make decisions confidently.</p>
    </article>

    <article class="value value--green">
      <svg class="value__shape" viewBox="0 0 120 318" width="120" height="318">
        <polygon points="0,70 20,56 100,56 120,70 120,278 60,318 0,278" fill="var(--card)"/>
        <polygon points="60,0 108,26 108,80 60,106 12,80 12,26" fill="var(--green)"/>
      </svg>
      <div class="value__icon" role="img" aria-label="Standing figure icon"></div>
      <h2 class="value__name">Be a Good<br>Human</h2>
      <p class="value__text">Treat everyone with kindness and respect. Act with honesty, listen well and do the right thing even when nobody watches.</p>
    </article>
  </section>

  <footer class="footer">
    <div class="brand">
      <span class="brand__mark"></span>
      <span class="brand__name">Brivora</span>
    </div>
    <span class="footer__company">Brivora Australia</span>
    <span class="footer__web">www.brivora.com.au</span>
  </footer>
</main>
</body>
</html>
```